Presentation Folder for dental clinic

We need a presentation folder design. The presentation folder is what we give to our patients with treatment plans, quotes, images, information sheets etc.
I have uploaded current stationary designs for assistance as well as a photo of our external sign design.
We are an upmarket dental clinic.
Professionalism and customer service is key to us.
We provide information in presentation folders to give to patients.
It needs to memorable and a statement to who we are.

Target Market(s)

Main patient base is Male and Female 40 years old to 70 years old

Industry/Entity Type

Dental Clinic

Font styles to use
Serif
Sans Serif

Requirements
Must have
• Design:
• -Professional
• -Timeless
• -Modern
• - Memorable
• - Statement (if a patient puts down the folder, it will be easily identifiable with as Morvel Dentals folder)
• Logo
• Address, phone, email, website
• Dr Leon Brisco name and degree details
• Colour scheme to match current logos and branding
• "Your Smile Our Passion" quote
Nice to have
• Services listed:
• - Sleep Dentistry
• - Happy Gas
• - Dental Implants
• - Cosmetic Dentistry
• - Oral Surgery
• - Clearotune
• - Teeth Whitening
• - General Dentistry
• - Childrens Dentistry
• See website www.morveldental.com.au
Should not have
• Dental cliche photos

```html
<!DOCTYPE html>
<html lang="en">
<head>
<meta charset="utf-8">
<title>Morvel Dental – Presentation Folder</title>
<link rel="stylesheet" href="https://fonts.googleapis.com/css2?family=Montserrat:wght@500&family=Open+Sans:wght@400&family=Kaushan+Script&display=swap">
<style>
  :root {
    --purple: #7d4391;
    --purple-deep: #6a3580;
    --purple-soft: #9a72a8;
    --white: #f4f4f4;
    --grey-text: #9a9a9a;
    --backdrop: #b9b9b9;
  }
  * { margin: 0; padding: 0; box-sizing: border-box; }
  html, body { width: 1200px; height: 800px; overflow: hidden; }
  body {
    background: var(--backdrop);
    position: relative;
    font-family: "Open Sans", sans-serif;
  }
  .folder-cover,
  .folder-inside {
    position: absolute;
    top: 100px;
    width: 450px;
    height: 600px;
    border-radius: 0 14px 14px 0;
    overflow: hidden;
  }
  .folder-cover { left: 120px; }
  .folder-inside { left: 630px; background: var(--white); }
  .folder-cover svg,
  .folder-inside svg { position: absolute; inset: 0; }

  .brand-name {
    position: absolute;
    left: 0;
    width: 450px;
    top: 158px;
    text-align: center;
    font-family: "Montserrat", sans-serif;
    font-weight: 500;
    font-size: 46px;
    letter-spacing: 0.5px;
    color: var(--purple);
  }
  .tagline {
    font-family: "Kaushan Script", cursive;
    font-size: 35px;
  }
  .tagline .muted { fill: var(--grey-text); }
  .tagline .accent { fill: var(--purple); }

  .services { list-style: none; }
  .services-group {
    position: absolute;
    top: 539px;
    font-size: 9px;
    line-height: 10px;
    color: var(--purple);
  }
  .services-group.first { left: 38px; }
  .services-group.second { left: 188px; }
  .services-group.third { left: 336px; }
</style>
</head>
<body>

  <section class="folder-cover" aria-label="Folder front cover">
    <svg width="450" height="600" viewBox="0 0 450 600">
      <rect width="450" height="600" fill="var(--purple)"/>
      <path d="M0 78 Q170 40 450 112 L450 340 L0 298 Z" fill="var(--white)"/>
      <path d="M0 310 L450 354 L450 420 L0 374 Z" fill="var(--white)"/>
      <path d="M0 390 L450 438" stroke="var(--white)" stroke-width="5" fill="none"/>
      <path d="M0 406 L450 458" stroke="var(--white)" stroke-width="4" fill="none"/>
      <rect x="0" y="528" width="450" height="52" fill="var(--white)"/>
      <path d="M135 528 L160 580 M285 528 L310 580" stroke="var(--purple)" stroke-width="3"/>
      <text class="tagline" x="34" y="356" transform="rotate(7 34 356)"><tspan class="muted">Your </tspan><tspan class="accent">Smile </tspan><tspan class="muted">Our </tspan><tspan class="accent">Passion</tspan></text>
    </svg>

    <h1 class="brand-name">Morvel Dental</h1>

    <ul class="services">
      <li class="services-group first">Sleep Dentistry<br>Happy Gas<br>Dental Implants</li>
      <li class="services-group second">Oral Surgery<br>Clearotune<br>Cosmetic Dentistry</li>
      <li class="services-group third">Teeth Whitening<br>General Dentistry<br>Childrens Dentistry</li>
    </ul>
  </section>

  <section class="folder-inside" aria-label="Folder inside with pocket">
    <svg width="450" height="600" viewBox="0 0 450 600" aria-hidden="true">
      <defs>
        <linearGradient id="pocket-shade" x1="0" y1="0" x2="1" y2="0">
          <stop offset="0" stop-color="var(--purple-deep)"/>
          <stop offset="0.55" stop-color="var(--purple-soft)"/>
          <stop offset="1" stop-color="var(--purple)"/>
        </linearGradient>
      </defs>
      <rect x="0" y="390" width="450" height="210" fill="url(#pocket-shade)"/>
    </svg>
  </section>

</body>
</html>
```